Resume: Professional Marketer seeking to impress potential recruiters with my skills & experience

Create a marketing esque style CV. I'm an outgoing, driven marketing with years of experience. I'm looking for a new senior role. My CV should look professional, but with elements of creativity and be a little bold. It should stand out amongst all the other CVs being submitted for a role. Check out my profilehub profile here: https://www.profilehub.example/in/marisol-upwick-58291034/ I would like to include a photo with the design, as a subtle element of the design.

Target Market(s)

Recruiters, Headhunters

Industry/Entity Type

Marketing

Font styles to use
Sans Serif

Requirements
Must have
• Easy to read sections, with enough detail for a recruiter to understand my experience.
Nice to have
• Graphics, icons etc to represent experience

```html
<!DOCTYPE html>
<html lang="en">
<head>
<meta charset="utf-8">
<title>Marisol Upwick – Resume</title>
<link href="https://fonts.googleapis.com/css2?family=Roboto:wght@400;500;700&display=swap" rel="stylesheet">
<style>
:root{
  --blue:#4a5cab;
  --green:#21a24b;
  --green-soft:#5fae6e;
  --bg:#b8b8b8;
  --paper:#ffffff;
}
*{box-sizing:border-box;margin:0;padding:0}
html,body{width:1200px;height:823px;overflow:hidden;background:var(--bg);font-family:'Roboto',sans-serif}
.canvas{position:relative;width:1200px;height:823px}
.page{position:absolute;background:var(--paper)}
.page--front{left:49px;top:30px;width:517px;height:731px}
.page--back{left:619px;top:48px;width:519px;height:729px}
.abs{position:absolute}

/* front */
.photo{left:8px;top:8px;width:128px;height:132px;border:3px solid var(--blue);border-radius:12px;background:linear-gradient(160deg,#8a9a6a,#d8a98a 55%,#c98f74);z-index:2}
.head-band{left:136px;top:18px;width:381px;height:63px;background:var(--blue);color:#fff;padding:10px 0 0 14px}
.name{font-size:29px;font-weight:500;letter-spacing:.5px;line-height:1}
.role{font-size:12px;margin-top:7px}
.contact-bar{left:139px;width:378px;height:20px;background:var(--blue);color:#fff;font-size:12px;display:flex;align-items:center;padding-left:8px;gap:8px;white-space:nowrap}
.contact-bar svg{flex:none}
.contact-bar .gap{margin-left:12px}
.sq{width:13px;height:13px;background:#fff;flex:none}
.section-title{display:flex;align-items:center;gap:6px;color:var(--blue);font-size:15px;font-weight:500;white-space:nowrap}
.ico{width:24px;height:24px;background:var(--blue);border-radius:4px;display:flex;align-items:center;justify-content:center;flex:none}
.rule{height:1px;background:var(--blue)}
.intro{left:18px;top:173px;width:489px;height:136px;border-radius:14px;background:linear-gradient(90deg,#66b16c,#4d7fa0 60%,var(--blue));color:#fff;font-size:9.7px;line-height:12.1px;text-align:justify;padding:10px 9px}
.intro p{text-indent:20px}
.skills{top:352px;font-size:9.8px;line-height:12.5px;color:var(--blue);list-style:none;white-space:nowrap}
.edu-head,.award-head{color:var(--blue);font-size:17px;font-weight:700;display:flex;align-items:center;gap:8px}
.edu{right:277px;text-align:right;font-size:8px;line-height:9.8px;color:var(--green);white-space:nowrap}
.edu b{display:block;color:var(--blue);font-size:10px;line-height:13px;font-weight:700}
.edu b.big{font-size:11px}
.edu-line{left:249px;top:524px;width:2px;height:190px;background:linear-gradient(var(--blue),var(--green-soft))}
.dot{width:7px;height:7px;border-radius:50%;background:var(--blue);left:246.5px}
.award{left:264px;width:250px;text-align:center;font-size:8px;line-height:9.8px;color:var(--green);white-space:nowrap}
.award span{display:block;color:var(--blue);font-size:10.5px;line-height:14px;text-decoration:underline}
.contact-box{left:276px;top:673px;width:216px;height:58px;background:var(--green);border-radius:10px 10px 0 0;color:#fff;text-align:right;padding:9px 10px 0 0;white-space:nowrap}
.contact-box .cta{font-size:15.5px}
.contact-box .line{font-size:10px;margin-top:4px}

/* back */
.back-band{left:0;top:0;width:519px;height:39px;background:var(--blue);color:#fff}
.back-name{left:23px;top:9px;font-size:12.5px;font-weight:500}
.back-role{left:21px;top:25px;font-size:8.5px}
.back-contact{left:268px;top:13px;font-size:12px;display:flex;align-items:center;gap:10px;white-space:nowrap}
.record-title{left:0;top:55px;width:100%;text-align:center;color:var(--blue);font-size:14.5px;font-weight:500}
.timeline{left:36px;top:76px;width:2px;height:640px;background:linear-gradient(var(--blue),var(--green))}
.job{left:38px;padding-left:15px;font-size:11.5px;line-height:14px;color:var(--blue);white-space:nowrap}
.job::before{content:"";position:absolute;left:0;top:7px;width:11px;height:2px;background:var(--green)}
.job h3{font-weight:400;font-size:13.8px;line-height:16px;color:var(--green)}
.job h3.inline{display:inline}
.job small{font-size:10.5px;color:var(--green);margin-left:6px}
.job .date{font-size:10.5px;color:var(--green)}
.job .fine{font-size:9.5px}
</style>
</head>
<body>
<div class="canvas">

  <section class="page page--front">
    <div class="abs photo" role="img" aria-label="Portrait photo of Marisol Upwick"></div>
    <header class="abs head-band">
      <div class="name">MARISOL UPWICK</div>
      <div class="role">Marketing Strategy Consultan</div>
    </header>
    <div class="abs contact-bar" style="top:85px">
      <svg width="12" height="14" viewBox="0 0 12 14"><path d="M6 0a5 5 0 0 1 5 5c0 3.5-5 9-5 9S1 8.5 1 5a5 5 0 0 1 5-5z" fill="#fff"/><circle cx="6" cy="5" r="2" fill="var(--blue)"/></svg>
      <span>Harbour Vale NSW</span>
      <svg class="gap" width="14" height="14" viewBox="0 0 14 14"><rect width="14" height="14" rx="3" fill="#fff"/><path d="M4 3l2 2-1 1.3c.7 1.3 1.7 2.3 3 3L9.3 8l2 2-1.2 1.5C6.5 11 3 7.5 2.5 3.9z" fill="var(--blue)"/></svg>
      <span>0400 555 019</span>
    </div>
    <div class="abs contact-bar" style="top:110px">
      <span class="sq"></span>
      <span>https://www.profilehub.example/in/marisol-upwick-58291034/</span>
    </div>

    <div class="abs section-title" style="left:143px;top:141px">
      <span class="ico"><svg width="14" height="14" viewBox="0 0 14 14"><circle cx="7" cy="4" r="3" fill="#fff"/><path d="M1 14c0-4 2.5-6 6-6s6 2 6 6z" fill="#fff"/></svg></span>
      INTRODUCTION
    </div>
    <div class="abs rule" style="left:290px;top:153px;width:227px"></div>

    <div class="abs intro">
      <p>I am a passionate direct marketer of 15+ years experience in Australia, plus key roles in startup organisations in London and New York.</p>
      <p>I am a talented consumer marketer with strong commercial and business acumen. I played a fundamental role in the growth of CoverWise Pty Ltd, to become the number one direct life insurance brand in Australia.</p>
      <p>As a strategic marketer, my strengths lie in analytical thinking and the ability to translate marketing and sales activity into commercial modeling, and ultimately profitability.</p>
      <p>I am a talented professional with the drive to succeed. I have benefited from working alongside exceptional people, who have helped me develop personally, and as a leader. My goals are to engage with as many strategic and intellectual minds as possible, and to help others develop to achieve theirs.</p>
    </div>

    <div class="abs section-title" style="left:12px;top:317px">
      <span class="ico" style="width:26px;height:26px"><svg width="14" height="14" viewBox="0 0 14 14"><circle cx="7" cy="4" r="3" fill="#fff"/><path d="M1 14c0-4 2.5-6 6-6s6 2 6 6z" fill="#fff"/></svg></span>
      KEY SKILLS AND EXPERIENCE
    </div>
    <div class="abs rule" style="left:246px;top:330px;width:271px"></div>

    <ul class="abs skills" style="left:46px">
      <li>Advertising</li><li>Branding</li><li>Budgeting &amp; Forecasting</li><li>Business Analysis</li><li>Call Centres</li><li>Customer Acquisition</li><li>Customer Retention</li><li>Copy Writing</li>
    </ul>
    <ul class="abs skills" style="left:221px">
      <li>Digital Marketing</li><li>Distribution</li><li>Direct Marketing</li><li>Executive Reporting</li><li>Financial Modelling</li><li>Lead Generation</li><li>Marketing Analysis</li><li>Marketing</li>
    </ul>
    <ul class="abs skills" style="left:365px">
      <li>Media Planning</li><li>People Management</li><li>Product Development</li><li>P&amp;L Responsibility</li><li>Retention</li><li>Sales</li><li>Strategy Development</li><li>Stakeholder Management</li>
    </ul>

    <div class="abs section-title" style="left:18px;top:465px;font-size:14.5px">
      <span class="ico" style="width:26px;height:28px"><svg width="14" height="16" viewBox="0 0 14 16"><path d="M3 1h10v12H4a2 2 0 0 0 0 2h9" fill="none" stroke="#fff" stroke-width="1.6"/><path d="M3 1v12" stroke="#fff" stroke-width="1.6"/></svg></span>
      QUALIFICATIONS:
    </div>
    <div class="abs rule" style="left:175px;top:479px;width:336px"></div>

    <div class="abs edu-head" style="left:38px;top:507px">
      <svg width="34" height="22" viewBox="0 0 34 22"><path d="M17 1L1 8l16 7 16-7z" fill="var(--blue)"/><path d="M8 11v6c3 3 15 3 18 0v-6l-9 4z" fill="var(--blue)"/><path d="M30 9v8" stroke="var(--blue)" stroke-width="1.5"/></svg>
      Education
    </div>
    <div class="abs edu-line"></div>
    <div class="abs dot" style="top:541px"></div>
    <div class="abs dot" style="top:593px"></div>
    <div class="abs dot" style="top:635px"></div>
    <div class="abs dot" style="top:676px"></div>

    <div class="abs edu" style="top:538px"><b class="big">BACHELOR OF BUSINESS</b>University of Applied Studies, Sydney<br>Major in Marketing and Small Business<br>January 1993 to june 1997</div>
    <div class="abs edu" style="top:590px"><b>Certificate IV In Business,Frontline Management</b>Academy South Metro, VIC<br>Completed october 2008</div>
    <div class="abs edu" style="top:632px"><b>Equip Leadership Program</b>Tallis Group<br>February 2009 to April 2010</div>
    <div class="abs edu" style="top:673px"><b>Tallis Senior Leaders Strategy Program</b>Tallis Group<br>April 2012 to Current</div>

    <div class="abs award-head" style="left:342px;top:504px">
      <svg width="20" height="20" viewBox="0 0 20 20"><path d="M5 1h10v6a5 5 0 0 1-10 0z" fill="var(--blue)"/><path d="M5 3H1c0 4 2 5 4 5M15 3h4c0 4-2 5-4 5" fill="none" stroke="var(--blue)" stroke-width="1.6"/><path d="M9 12h2v4H9zM5 17h10v2H5z" fill="var(--blue)"/></svg>
      Awards
    </div>
    <div class="abs award" style="top:531px"><span>Employee of the Year Award 2005</span>CoverWise Pty Ltd<br>December 2005</div>
    <div class="abs award" style="top:577px"><span>Outstanding Achievement Award 2008</span>Tallis Group<br>December 2008</div>
    <div class="abs award" style="top:619px"><span>Overall Company Achievement&nbsp; Award 2009</span>Tallis Group<br>December 2009</div>

    <div class="abs contact-box">
      <div class="cta">Contact me</div>
      <div class="line">marisolu04@mail.example or 0400 555 019</div>
    </div>
  </section>

  <section class="page page--back">
    <header class="abs back-band">
      <div class="abs back-name">MARISOL UPWICK</div>
      <div class="abs back-role">Marketing Strategy Consultan</div>
      <div class="abs back-contact">
        <svg width="11" height="14" viewBox="0 0 12 14"><path d="M6 0a5 5 0 0 1 5 5c0 3.5-5 9-5 9S1 8.5 1 5a5 5 0 0 1 5-5z" fill="#fff"/><circle cx="6" cy="5" r="2" fill="var(--blue)"/></svg>
        <span>Harbour Vale NSW</span>
        <svg width="14" height="14" viewBox="0 0 14 14"><rect width="14" height="14" rx="3" fill="#fff"/><path d="M4 3l2 2-1 1.3c.7 1.3 1.7 2.3 3 3L9.3 8l2 2-1.2 1.5C6.5 11 3 7.5 2.5 3.9z" fill="var(--blue)"/></svg>
        <span>0400 555 019</span>
      </div>
    </header>

    <h2 class="abs record-title">EMPLOYMENT RECORD (last 15 years)</h2>
    <div class="abs timeline"></div>

    <div class="abs job" style="top:76px"><h3>MARKETING STRATEGY CONSULTANT</h3>Clients include PedalNotes, Alpine Re, Tayne Sydney, Supper Delivered<br><span class="date">May 2016 to Current</span></div>
    <div class="abs job" style="top:133px"><h3>MARKETER AND BUSINESS DEVELOPMENT</h3>Mark Gunnell Photography <small>January 2011to Current</small></div>
    <div class="abs job" style="top:173px"><h3 class="inline">Career break</h3> <small style="margin-left:16px">August 2015 to May 2016</small></div>
    <div class="abs job" style="top:195px"><h3>HEAD OF MARKETING</h3>Global Cover Distribution (US) Treasure Life (life insurance brand)<br><span class="date">April 2015 `to August 2015</span></div>
    <div class="abs job" style="top:254px"><h3 class="inline">Maternity Leave - to my son Leo</h3> <small>August 2014 to April 2015</small></div>
    <div class="abs job" style="top:283px"><h3 class="inline">Career break</h3> <small>May 2103 to April 2014</small></div>
    <div class="abs job" style="top:311px"><h3>CONSULTANT – NEW BUSINESS PROPOSAL</h3>Clearpath Administration Services Pty Limited <small>October 2013</small></div>
    <div class="abs job" style="top:354px"><h3>COMMERCIAL &amp; MIS MANAGER</h3>Tallis Group <small style="margin-left:14px">December 2012to May 2013</small></div>
    <div class="abs job" style="top:400px"><h3>HEAD OF MARKETING OPERATIONS – ACQUISITION AND RETENTION</h3>Tallis Group <small>July 2012 to December 2012</small></div>
    <div class="abs job" style="top:439px"><h3>P&amp;L / BRAND MANAGER – COVERWISE</h3>Tallis Group <small>October 2010 to July 2012</small></div>
    <div class="abs job" style="top:480px"><h3>Product Portfolio Marketing Manager – CoverWise</h3>Tallis Group <small>January 2010 to October 2010</small></div>
    <div class="abs job" style="top:518px"><h3>Marketing Manager – CoverWise</h3><span class="fine">Tallis Group (CoverWise Pty Limited was acquired by Tallis Group in September 2008)</span><br><span class="date">January 2008 to October 2010</span></div>
    <div class="abs job" style="top:570px"><h3>Database and Retention Strategy Manager</h3>CoverWise Pty Limited Melbourne Office relocation<br><span class="date">February 2007 to December 2007</span></div>
    <div class="abs job" style="top:624px"><h3>DIRECT MARKETING SPECIALIST</h3>CoverWise Pty Limited <small>July 2004 to January 2007</small></div>
    <div class="abs job" style="top:664px"><h3>ACQUISITION AND DATABASE MARKETING MANAGER - JAPAN</h3>Prizeworks Pty Ltd(currently known as Mailworks Pty Ltd)<br><span class="date">April 2002to June 2004</span></div>
  </section>

</div>
</body>
</html>
```